Software Company Business Card Design

We are looking for a business card design for a software, messaging & IT services company based in Australia.

Talvora Group is the holding company for 3 brands all offering technology based business solutions; Talvora, Brindle & Quillpad. Brand Identity = Friendly, Professional, Viable, Vibrant, Creative

We want our business card to reflect that we are an innovative market leader. The design should be clean, professional and original.

This design will be used for all 3 brands.

More information about our company can be found at: www.talvoragroup.example.au
www.brindle.example.au

Details we would like on the card:

Firstname Lastname
Position
Level 17, 482 Ormond Rd
North Sydney
NSW 2060
Phone: +61 2 5550 1738
Fax: +61 2 5550 1794
Mobile:
Email:
www.talvoragroup.example.au

Target Market(s)

Our business cards are given to B2B and industry professionals.

Industry/Entity Type

Business

Requirements
Must have
• The Business Card must include the same colours as the logo.
Nice to have
• We would like it to me double sided.

```html
<!DOCTYPE html>
<html lang="en">
<head>
<meta charset="utf-8">
<title>Talvora Group – Business Card</title>
<link rel="stylesheet" href="https://fonts.googleapis.com/css2?family=Sorts+Mill+Goudy:ital@0;1&display=swap">
<style>
  :root {
    --page: #ffffff;
    --lavender: #9c9ec6;
    --lavender-light: #a7a9ce;
    --lavender-deep: #8f92bc;
    --texture-dark: #8c8fb8;
    --panel-red: #cf3a3a;
    --panel-red-light: #eab0b0;
    --brand-crimson: #a8163c;
    --brand-on-red: #f4f0f6;
    --name-olive: #c9b84a;
    --contact-ink: #f2f2f8;
    --web-ink: #2c2f66;
    --serif: "Sorts Mill Goudy", Georgia, serif;
  }

  html, body {
    margin: 0;
    padding: 0;
  }

  body {
    width: 1200px;
    height: 848px;
    overflow: hidden;
    background: var(--page);
    position: relative;
    font-family: var(--serif);
  }

  .card {
    position: absolute;
    width: 605px;
    height: 386px;
    box-shadow: 6px 8px 14px rgba(60, 60, 80, 0.35);
    overflow: hidden;
  }

  /* Front side */
  .card--front {
    left: 88px;
    top: 25px;
    background: var(--lavender);
  }

  .front__details {
    position: absolute;
    left: 0;
    top: 0;
    width: 433px;
    height: 100%;
    background: linear-gradient(180deg, var(--lavender-light) 0%, var(--lavender) 55%, var(--lavender-deep) 100%);
  }

  .front__name {
    position: absolute;
    left: 32px;
    top: 46px;
    margin: 0;
    font-style: italic;
    font-weight: 400;
    font-size: 20px;
    letter-spacing: 0.5px;
    color: var(--name-olive);
    text-shadow: 3px 4px 5px rgba(40, 40, 60, 0.55);
  }

  .front__contact {
    position: absolute;
    left: 32px;
    top: 84px;
    margin: 0;
    padding: 0;
    list-style: none;
    font-size: 20px;
    line-height: 27.8px;
    color: var(--contact-ink);
    letter-spacing: 0.6px;
  }

  .front__web {
    position: absolute;
    left: 110px;
    top: 340px;
    margin: 0;
    font-style: italic;
    font-size: 22px;
    color: var(--web-ink);
    text-shadow: 3px 4px 5px rgba(40, 40, 60, 0.45);
  }

  .front__brand-panel {
    position: absolute;
    left: 433px;
    top: 0;
    width: 172px;
    height: 100%;
    background:
      radial-gradient(ellipse 170px 70px at 100% 0%, var(--panel-red-light) 0%, rgba(234, 176, 176, 0) 100%),
      var(--panel-red);
  }

  .front__brand {
    position: absolute;
    right: 14px;
    top: 40px;
    margin: 0;
    text-align: right;
    color: var(--brand-on-red);
    font-weight: 400;
    line-height: 1;
  }

  .front__brand-main {
    display: block;
    font-size: 42px;
  }

  .front__brand-sub {
    display: block;
    font-size: 18px;
    margin-top: 4px;
  }

  /* Back side */
  .card--back {
    left: 453px;
    top: 425px;
  }

  .back__texture {
    position: absolute;
    inset: 0;
    background:
      radial-gradient(ellipse 420px 260px at 70% 70%, var(--texture-dark) 0%, rgba(140, 143, 184, 0) 100%),
      linear-gradient(160deg, var(--lavender-light) 0%, var(--lavender) 50%, var(--lavender-deep) 100%);
  }

  .back__brand {
    position: absolute;
    left: 14px;
    top: 22px;
    width: 352px;
    margin: 0;
    color: var(--brand-crimson);
    font-weight: 400;
    line-height: 1;
    text-align: right;
  }

  .back__brand-main {
    display: block;
    font-size: 104px;
    text-align: left;
  }

  .back__brand-sub {
    display: block;
    font-size: 42px;
    margin-top: 2px;
  }
</style>
</head>
<body>

  <section class="card card--front" aria-label="Card front">
    <div class="front__details">
      <h1 class="front__name">FIRST NAME LAST NAME</h1>
      <ul class="front__contact">
        <li>postion</li>
        <li>level 17,482 Ormond</li>
        <li>Rd</li>
        <li>North Sydney</li>
        <li>NSW 2060</li>
        <li>Phone:+61255501738</li>
        <li>Fax:+61255501794</li>
        <li>Mobile:</li>
        <li>Email:</li>
      </ul>
      <p class="front__web">www.talvoragroup.example.au</p>
    </div>
    <div class="front__brand-panel">
      <p class="front__brand">
        <span class="front__brand-main">Talvora</span>
        <span class="front__brand-sub">Group</span>
      </p>
    </div>
  </section>

  <section class="card card--back" aria-label="Card back">
    <div class="back__texture" role="img" aria-label="Soft embossed lavender surface texture"></div>
    <p class="back__brand">
      <span class="back__brand-main">Talvora</span>
      <span class="back__brand-sub">Group</span>
    </p>
  </section>

</body>
</html>
```